Corporate Capability Brochure for LumoByte

Create Corporate Capability Brochure for Executive IT Consulting Firm. Minority Business Enterprise (MBE) and Service Disabled Veteran Owned Small Business (SDVOSB). LumoByte is an Executive Information Technology Consulting Firm. We specialize in combining people with technology to deliver the Business of IT. We partner with C-Level Executives and their organizations to leverage technology that drives innovation and accelerates business transformation and enable businesses, governments and educational institutions to operate more successfully in a world where everything is increasingly linked together.

Looking for something clean, professional, innovative, eye-catching and creates a strong presence. The final design should communicate our numerous service offerings.

We are in the processing of updating our website so please use information obtained from capability statement uploaded. PLEASE USE LUMOBYTE CAPABILITY STATEMENT-COMMERCIAL (FILE 1) for content to be used in flyer/brochure being requested. Presentation was uploaded as a document to gauge style. We are still in the process of finding our style when it comes to marketing materials. Creativity is highly welcomed.

Target Market(s)

C-Level Executives. We work with Education Institutions, Healthcare Agencies, Federal Government Clients, Sports and Entertainment Companies and Technology companies.

Industry/Entity Type

Information Technology

Requirements
Should not have
• No Dark Backgrounds that make it hard to see
• No playful fonts that come across unprofessional
• Would prefer not to have images of people-Unless image provides Diversity

```html
<!DOCTYPE html>
<html lang="en">
<head>
<meta charset="utf-8">
<title>LumoByte Capability Brochure</title>
<link href="https://fonts.googleapis.com/css2?family=Montserrat:wght@300;400;600;700&display=swap" rel="stylesheet">
<style>
  :root {
    --brand-red: #b3151f;
    --deep-red: #7d0d14;
    --panel-red: rgba(110, 10, 16, 0.45);
    --ink: #1b1b1b;
    --white: #ffffff;
    --page-bg: #e9e6e3;
    --sky: #9cc3e0;
    --city-gray: #7b7f7c;
    --city-green: #5c6b4f;
  }
  * { margin: 0; padding: 0; box-sizing: border-box; }
  html, body { width: 1200px; height: 960px; overflow: hidden; }
  body { background: var(--page-bg); font-family: "Montserrat", sans-serif; position: relative; }

  .brochure {
    position: absolute; left: 280px; top: 33px;
    width: 668px; height: 934px;
    transform: scale(0.958); transform-origin: top left;
    background: var(--brand-red); overflow: hidden; color: var(--white);
    box-shadow: 0 6px 24px rgba(0,0,0,0.25);
  }
  .brochure-shapes { position: absolute; inset: 0; }

  .brand { position: absolute; left: 22px; top: 30px; display: flex; align-items: center; gap: 6px; }
  .brand-square { width: 12px; height: 12px; background: var(--brand-red); }
  .brand-name { font-size: 14px; font-weight: 700; color: var(--brand-red); }

  .headline { position: absolute; left: 28px; top: 192px; }
  .headline-line {
    display: block; width: max-content; background: var(--ink);
    font-size: 34px; font-weight: 600; line-height: 48px; padding: 0 8px 0 2px;
  }

  .focus-areas { position: absolute; left: 28px; top: 360px; font-size: 16.5px; font-weight: 600; white-space: nowrap; }
  .focus-areas .divider { margin: 0 9px; }

  .intro { position: absolute; left: 28px; top: 396px; width: 330px; font-size: 10.5px; font-weight: 700; line-height: 14.5px; }

  .services-panel { position: absolute; left: 0; top: 455px; width: 480px; height: 142px; background: var(--panel-red); padding: 12px 28px 0 30px; }
  .services-title { display: flex; align-items: center; gap: 6px; font-size: 22px; font-weight: 600; margin-bottom: 6px; }
  .services-panel p { font-size: 10.5px; font-weight: 300; line-height: 14.5px; }

  .service-copy { position: absolute; left: 28px; width: 480px; font-size: 10.5px; font-weight: 300; line-height: 14.6px; }
  .service-copy p + p { margin-top: 14px; }
  .copy-solutions { top: 600px; }

  .advisory-panel { position: absolute; left: 0; top: 760px; width: 522px; height: 174px; background: var(--panel-red); padding: 6px 0 0 28px; }
  .advisory-panel p { font-size: 10.5px; font-weight: 300; line-height: 14.6px; width: 482px; }
</style>
</head>
<body>
  <article class="brochure">
    <svg class="brochure-shapes" width="668" height="934" viewBox="0 0 668 934">
      <defs>
        <linearGradient id="cityTones" x1="0" y1="0" x2="0" y2="1">
          <stop offset="0" stop-color="#cfe2f1"/>
          <stop offset="0.07" stop-color="var(--sky)"/>
          <stop offset="0.12" stop-color="var(--city-green)"/>
          <stop offset="0.45" stop-color="var(--city-gray)"/>
          <stop offset="1" stop-color="#8e8a84"/>
        </linearGradient>
      </defs>
      <polygon points="0,0 668,0 668,683 150,52 0,130" fill="url(#cityTones)" role="img" aria-label="Aerial photograph of a downtown city skyline"/>
      <polygon points="0,130 150,52 160,64 0,150" fill="var(--deep-red)"/>
      <polygon points="0,0 155,50 0,140" fill="var(--white)"/>
      <polygon points="520,862 668,770 668,788 538,870" fill="var(--deep-red)"/>
      <polygon points="525,858 668,780 668,934 668,934" fill="var(--white)"/>
      <polygon points="525,858 668,934 668,780" fill="var(--white)"/>
      <circle cx="638" cy="835" r="22" fill="#2b4fa0" role="img" aria-label="Certification badge"/>
      <circle cx="638" cy="890" r="22" fill="#1f3f94" role="img" aria-label="Certification badge"/>
    </svg>

    <div class="brand"><span class="brand-square"></span><span class="brand-name">LumoByte</span></div>

    <h1 class="headline">
      <span class="headline-line">Strategic</span>
      <span class="headline-line">Guidance</span>
      <span class="headline-line">and Actionable Results</span>
    </h1>

    <p class="focus-areas">Unified Communications<span class="divider">|</span>Network<span class="divider">|</span>Data Center</p>

    <p class="intro">At LumoByte we are not concerned about the sale, we are concerned about the customer. We believe that taking care of the real needs of our customers regardless of technology. Our business are built on relationships and doing the right</p>

    <section class="services-panel">
      <h2 class="services-title">
        <svg width="40" height="40" viewBox="0 0 40 40" fill="none" stroke="#fff" stroke-width="1.4">
          <circle cx="20" cy="20" r="5"/><circle cx="20" cy="5" r="3"/><circle cx="20" cy="35" r="3"/>
          <circle cx="6" cy="13" r="3"/><circle cx="34" cy="13" r="3"/><circle cx="6" cy="27" r="3"/><circle cx="34" cy="27" r="3"/>
          <path d="M20 8v7M20 25v7M8.6 14.5l7 3.5M31.4 14.5l-7 3.5M8.6 25.5l7-3.5M31.4 25.5l-7-3.5"/>
        </svg>
        Our Services:
      </h2>
      <p>LumoByte's passion for the Business of IT and our commitment to quality results means we focus on the right solutions to meet your specific needs. Our focus on understanding, quantifying and measuring business results is a unique differentiator that allows us to deliver high-value, high-touch solutions with proven ROI. Our suite of services includes:</p>
    </section>

    <div class="service-copy copy-solutions">
      <p>Solutions-as-a-Service<br>We provide end-to-end solutions, utilizing consulting methodologies that are refined by decades of experience, across multiple disciplines. Whether you are addressing network, compute, data protection, virtualization or security, we provide the resources and expertise that allow your company to reach its goals.</p>
      <p>Related Services:<br>Data Center Infrastructure, Data Center Facility Selection, Design and Build, Data Center Migration, Business Continuity and Disaster Recovery, Converged Infrastructure, Collaboration &amp; Mobility, External Infrastructure Strategy &amp; Selection.</p>
    </div>

    <section class="advisory-panel">
      <p>Related Services:<br>Strategy Assessments, Executive Advising, CTO/CIO On Demand, Virtual CTO/CIO<br>Technology Business Management (TBM)-as-a-Service<br>We help clients navigate the changing landscape at the intersection of Business and Technology enabling them to improve the way they make technology decisions. This allows them to optimize costs, quality and the overall value of their IT services.<br>Related Services:<br>Cloud Migration Programs, Cloud Strategy Roadmap Planning, Data Center &amp; Vendor Consolidation, Application Rationalization, Infrastructure Technology Assessment, IT Organization Change Management, IT Budget and Forecasting Process, Infrastructure Cost Savings Assessment</p>
    </section>
  </article>
</body>
</html>
```